WP website design (Pell)

We need a wordpress design for an established auction and real estate company based in Texas. The winning design will incorporate a professional color scheme with company logo in a clean layout. The design needs to consider that this will be developed on a responsive theme. Colors are those that will highlight the logo.

Reason: was waiting for updated logo

Industry/Entity Type

Real Estate

Font styles to use
Serif
Sans Serif

Requirements
Must have
• Navigation:
1) Home
2) Auctions
3) Online Auctions
4) Services
5) About Us
6) Contact us

Slideshow will be used - please use stock real estate photo. Tag line in the header - "Your Austin Auction Professionals!” Color of the site will be those in the logo and black.

Widgets - 1) Social media icons for twitter, facebook, linkedIn and Rss. 2) News & events blog, 3) Featured video, 4) Email Sign-up, 5) Testimonials

Company logo and contact info in the footer with attached logos too.
Nice to have
• Use of a drop down menu style - under 'Auctions'
1) Upcoming Auctions
2) Past Auctions

```html
<!DOCTYPE html>
<html lang="en">
<head>
<meta charset="utf-8">
<title>Pell Brothers Auction Service</title>
<link href="https://fonts.googleapis.com/css2?family=Source+Sans+3:ital,wght@0,300;0,400;0,600;0,700;1,400&display=swap" rel="stylesheet">
<style>
:root{
  --brand-blue:#3a3a9e;
  --brand-blue-dark:#2a2a80;
  --brand-blue-deep:#25256e;
  --brand-red:#d8262c;
  --accent-yellow:#ffc20e;
  --accent-yellow-light:#ffd24a;
  --panel-dark:rgba(28,28,30,.78);
  --text-light:#ffffff;
  --text-muted:#9a9a9a;
  --ink:#1b1b1b;
}
*{margin:0;padding:0;box-sizing:border-box}
html,body{width:1200px;height:1049px;overflow:hidden}
body{position:relative;font-family:"Source Sans 3",Arial,sans-serif;background:#fff;color:var(--ink)}
.abs{position:absolute}

/* header */
.site-header{left:0;top:0;width:1200px;height:147px;background:#fff}
.brand{left:110px;top:34px;width:160px;display:flex;align-items:center;gap:8px}
.brand-mark{width:14px;height:14px;background:var(--brand-red);flex:none}
.brand-name{font-weight:700;font-size:25px;line-height:1.1;color:var(--brand-blue);text-transform:uppercase;letter-spacing:.5px}
.brand-sub{position:absolute;left:132px;top:101px;font-weight:700;font-size:11px;color:var(--brand-blue);letter-spacing:2px}
.social{display:flex;gap:19px}
.social span{width:31px;height:31px;border-radius:3px;display:block;box-shadow:inset 0 -2px 0 rgba(0,0,0,.12)}
.s-a{background:linear-gradient(#ffc94a,#f2a20f)}
.s-b{background:linear-gradient(#8fd6f5,#4fb2e2)}
.s-c{background:linear-gradient(#7fcde8,#3d9dc7)}
.s-d{background:linear-gradient(#4a6fc0,#2b4a94)}
.header-social{left:907px;top:81px}

/* nav */
.main-nav{left:0;top:147px;width:1200px;height:58px;background:linear-gradient(#4646ae,#36369a)}
.nav-item{position:absolute;top:0;height:58px;line-height:58px;font-size:12.5px;color:var(--text-light);text-transform:uppercase;white-space:nowrap}
.nav-item.active{background:linear-gradient(var(--accent-yellow),#ffca2a);color:var(--ink);padding:0 13px;left:197px}
.dropdown{left:196px;top:205px;width:153px;height:88px;background:var(--accent-yellow-light);padding-top:22px}
.dropdown li{list-style:none;font-size:12px;color:var(--ink);padding-left:12px;height:25px;text-transform:uppercase}
.dropdown li::before{content:"\2192";margin-right:8px}

/* hero */
.hero{left:0;top:205px;width:1200px;height:632px;background:linear-gradient(105deg,#6d6a5c 0%,#5f5d8e 22%,#7a7bc4 48%,#8688c8 70%,#5b5a5c 100%)}
.tagline{left:111px;top:399px;width:476px;height:111px;background:var(--brand-blue-dark);opacity:.97;padding:18px 0 0 31px;color:var(--text-light)}
.tagline .t1{font-weight:300;font-size:31px;line-height:36px}
.tagline .t2{font-weight:700;font-size:33px;line-height:40px}
.dots{left:586px;top:584px;display:flex;gap:5px}
.dots i{width:5px;height:5px;border-radius:50%;background:#fff;opacity:.7;display:block}
.dots i.on{opacity:1;background:#ddd}

/* widgets */
.widget{background:var(--panel-dark);color:var(--text-light)}
.widget h3{position:absolute;left:20px;top:14px;font-size:15px;font-weight:600}
.arrows{position:absolute;right:18px;top:15px;display:flex;gap:16px}
.arrows svg{display:block}
.news{left:111px;top:606px;width:309px;height:187px}
.news-thumb{left:17px;top:54px;width:89px;height:75px;background:linear-gradient(#6fa2d8 0%,#c9b58c 55%,#4e6b33 100%)}
.news-date{left:121px;top:53px;font-size:11.5px;color:var(--text-muted)}
.news-text{left:121px;top:85px;width:160px;font-size:11.5px;line-height:15.5px}
.news-more{left:20px;top:136px;width:258px;font-size:11.5px;line-height:15.5px}
.video{left:447px;top:606px;width:306px;height:187px}
.video-frame{left:18px;top:46px;width:275px;height:128px;background:linear-gradient(90deg,#d8d8d8,#eaeef0 50%,#9aa58a 75%,#cfd4d6)}
.play{left:133px;top:50px}
.testimonial{left:780px;top:606px;width:309px;height:111px;border-radius:4px}
.testimonial p{position:absolute;left:20px;top:43px;width:262px;font-size:11.5px;line-height:15.5px}
.pointer{left:1013px;top:717px}
.author{left:972px;top:737px;font-size:11.5px;font-style:italic;color:var(--text-light)}

/* footer */
.site-footer{left:0;top:837px;width:1200px;height:158px;background:linear-gradient(#3c3ca6,#3434a0)}
.footer-h{position:absolute;top:26px;font-size:15px;font-weight:400;color:var(--text-light);text-transform:uppercase}
.quick-links{position:absolute;left:112px;top:62px;list-style:none}
.quick-links li{font-size:11.5px;color:var(--text-light);height:20.6px}
.footer-social{left:267px;top:58px;gap:19px}
.footer-social span{width:31px;height:31px}
.subscribe-input{left:489px;top:64px;width:167px;height:48px;background:#fff;font-size:14px;color:#a6a6a6;padding:16px 0 0 11px}
.subscribe-btn{left:673px;top:64px;width:87px;height:48px;background:linear-gradient(var(--accent-yellow-light),var(--accent-yellow));font-size:12px;color:var(--ink);text-align:center;line-height:48px}
.partners{left:780px;top:30px;width:309px;height:86px;background:#fff;border-radius:6px}
.copyright{left:0;top:995px;width:1200px;height:54px;background:var(--brand-blue-deep);border-top:1px solid #4848ae;color:var(--text-light);font-size:11.5px;text-align:center;line-height:54px}
</style>
</head>
<body>

<header class="site-header abs">
  <div class="brand abs">
    <span class="brand-mark"></span>
    <span class="brand-name">Pell Brothers</span>
  </div>
  <div class="brand-sub">AUCTION SERVICE</div>
  <div class="social header-social abs" aria-label="Social links">
    <span class="s-a" role="img" aria-label="News feed link"></span>
    <span class="s-b" role="img" aria-label="Social link"></span>
    <span class="s-c" role="img" aria-label="Social link"></span>
    <span class="s-d" role="img" aria-label="Social link"></span>
  </div>
</header>

<nav class="main-nav abs">
  <span class="nav-item" style="left:121px">Home</span>
  <span class="nav-item active">Auctions</span>
  <span class="nav-item" style="left:321px">Online Auctions</span>
  <span class="nav-item" style="left:473px">About Us</span>
  <span class="nav-item" style="left:585px">Services</span>
  <span class="nav-item" style="left:691px">Real Estate Listings</span>
  <span class="nav-item" style="left:865px">References</span>
  <span class="nav-item" style="left:989px">Contact Us</span>
</nav>

<section class="hero abs" role="img" aria-label="Slideshow photo of a living room with a blue sofa, cushions and a potted plant"></section>

<ul class="dropdown abs">
  <li>Upcoming Auctions</li>
  <li>Past Auctions</li>
</ul>

<div class="tagline abs">
  <div class="t1">YOUR AUSTIN</div>
  <div class="t2">AUCTION PROFESSIONALS!</div>
</div>

<div class="dots abs"><i></i><i class="on"></i><i></i></div>

<article class="widget news abs">
  <h3>Latest News And Events</h3>
  <div class="arrows">
    <svg width="8" height="12" viewBox="0 0 8 12"><path d="M6 1 1 6l5 5" fill="none" stroke="#fff" stroke-width="1.6"/></svg>
    <svg width="8" height="12" viewBox="0 0 8 12"><path d="M2 1l5 5-5 5" fill="none" stroke="#fff" stroke-width="1.6"/></svg>
  </div>
  <div class="news-thumb abs" role="img" aria-label="Photo of a two-storey brick house"></div>
  <div class="news-date abs">Jun 14 2014</div>
  <p class="news-text abs">Neque porro quisquam est qui dolorem ipsum quia dolor sit amet, consectetur, adipisci</p>
  <p class="news-more abs">There is no one who loves pain itself, who seeks after it and wants to have it, simply because it is</p>
</article>

<article class="widget video abs">
  <h3>Featured Video</h3>
  <div class="arrows">
    <svg width="8" height="12" viewBox="0 0 8 12"><path d="M6 1 1 6l5 5" fill="none" stroke="#fff" stroke-width="1.6"/></svg>
    <svg width="8" height="12" viewBox="0 0 8 12"><path d="M2 1l5 5-5 5" fill="none" stroke="#fff" stroke-width="1.6"/></svg>
  </div>
  <div class="video-frame abs" role="img" aria-label="Video still of a bright living room with white sofa and garden view">
    <svg class="play abs" width="34" height="34" viewBox="0 0 34 34"><circle cx="17" cy="17" r="15.5" fill="rgba(255,255,255,.35)" stroke="#111" stroke-width="2"/><path d="M13 10l11 7-11 7z" fill="#111"/></svg>
  </div>
</article>

<article class="widget testimonial abs">
  <h3>Testimonial</h3>
  <div class="arrows">
    <svg width="8" height="12" viewBox="0 0 8 12"><path d="M6 1 1 6l5 5" fill="none" stroke="#fff" stroke-width="1.6"/></svg>
    <svg width="8" height="12" viewBox="0 0 8 12"><path d="M2 1l5 5-5 5" fill="none" stroke="#fff" stroke-width="1.6"/></svg>
  </div>
  <p>"Neque porro quisquam est qui dolorem ipsum quia dolor sit amet, consectetur, adipisci velit..."</p>
</article>
<svg class="pointer abs" width="20" height="16" viewBox="0 0 20 16"><path d="M0 0h20L10 16z" fill="rgba(28,28,30,.78)"/></svg>
<div class="author abs">-founder of Company -</div>

<footer class="site-footer abs">
  <h4 class="footer-h" style="left:112px">Quick Links</h4>
  <ul class="quick-links">
    <li>Home</li><li>Auctions</li><li>Online Auctions</li><li>About Us</li>
  </ul>
  <h4 class="footer-h" style="left:266px">Get Connect</h4>
  <div class="social footer-social abs" aria-label="Social links">
    <span class="s-a" role="img" aria-label="News feed link"></span>
    <span class="s-b" role="img" aria-label="Social link"></span>
    <span class="s-c" role="img" aria-label="Social link"></span>
    <span class="s-d" role="img" aria-label="Social link"></span>
  </div>
  <h4 class="footer-h" style="left:489px">Subscribe</h4>
  <div class="subscribe-input abs">Enter Your Maild Id</div>
  <div class="subscribe-btn abs">Subscribe</div>
  <div class="partners abs" aria-label="Partner and association badges">
    <svg width="309" height="86" viewBox="0 0 309 86">
      <rect x="12" y="18" width="50" height="52" rx="3" fill="#1b1b1b" role="img" aria-label="Auctioneers association badge"/>
      <rect x="72" y="30" width="168" height="28" rx="4" fill="#e8841c" role="img" aria-label="University badge"/>
      <circle cx="277" cy="43" r="27" fill="#b99a4a" role="img" aria-label="State association seal"/>
      <circle cx="277" cy="43" r="18" fill="#e6dcc0"/>
    </svg>
  </div>
</footer>

<div class="copyright abs">©2014 Pell.com &nbsp;|&nbsp; All right Reserved</div>

</body>
</html>
```